Mental Health and Marriage & Family Counseling Office Business Card Design

I work with a wide range of emotional and behavioral issues providing services that span from therapy for depression and grief counseling to parenting support, couples counseling and beyond. In a comfortable and supportive atmosphere, I offer a highly personalized approach tailored to each of my clients individual needs to help attain the personal growth they’re striving for. Providing individual, couples and family counseling.
Treatment specialization includes: Therapy for Depression and Anxiety, Couples Counseling, Family Counseling, Parenting Support, Grief Counseling, Work and Career issues, Stress Management, Conflict Resolution. I would like to see designs that use the colors "of a Peacock feather" , such as blues and greens, etc.

Industry/Entity Type

Business

Contact Information for Business Card

Delia K. Fenwick, MS, LPC
Licensed Professional Counselor
415 Harrowgate Lane Suite 231
Jacksonville, NC 28593

(910) 487-6124 Fax: (910) 487-6125
www.deliafenwicklpc.example
delia@deliafenwicklpc.example

```html
<!DOCTYPE html>
<html lang="en">
<head>
<meta charset="utf-8">
<title>Delia K. Fenwick, MS, LPC — Business Card</title>
<link rel="stylesheet" href="https://fonts.googleapis.com/css2?family=Poppins:wght@700&family=Questrial&family=Open+Sans:wght@400;600;700&display=swap">
<style>
  :root {
    --backdrop: #e4e4e4;
    --lime: #86c232;
    --lime-deep: #78b423;
    --green-text: #3aa53a;
    --navy: #1c57a5;
    --ink: #333333;
    --rule: #dcdcdc;
    --paper: #ffffff;
  }
  * { box-sizing: border-box; margin: 0; padding: 0; }
  html, body { width: 1200px; height: 852px; overflow: hidden; }
  body {
    background: var(--backdrop);
    font-family: "Open Sans", Arial, sans-serif;
    position: relative;
  }
  .card {
    position: absolute;
    left: 320px;
    width: 560px;
    height: 320px;
    border-radius: 18px;
    overflow: hidden;
    box-shadow: 0 6px 18px rgba(0,0,0,0.18);
  }
  /* Front */
  .card-front {
    top: 76px;
    background: linear-gradient(135deg, var(--lime) 0%, var(--lime-deep) 100%);
    display: flex;
    flex-direction: column;
    align-items: center;
    justify-content: center;
  }
  .wordmark {
    display: flex;
    align-items: center;
    gap: 12px;
  }
  .wordmark-dot {
    width: 30px; height: 30px;
    border-radius: 50%;
    background: var(--navy);
    flex: none;
  }
  .wordmark-name {
    font-family: "Poppins", Arial, sans-serif;
    font-weight: 700;
    font-size: 30px;
    color: var(--navy);
    letter-spacing: -0.3px;
    white-space: nowrap;
  }
  .card-front .tagline {
    font-family: "Questrial", Arial, sans-serif;
    color: var(--paper);
    font-size: 18px;
    margin-top: 4px;
  }
  /* Back */
  .card-back {
    top: 456px;
    background: var(--paper);
  }
  .card-back .lockup {
    position: absolute;
    left: 34px;
    top: 40px;
  }
  .card-back .wordmark-name { font-size: 26px; }
  .card-back .wordmark-dot { width: 26px; height: 26px; }
  .card-back .tagline {
    font-family: "Questrial", Arial, sans-serif;
    color: var(--green-text);
    font-size: 17px;
    margin: 2px 0 0 38px;
  }
  .person {
    position: absolute;
    left: 40px;
    top: 150px;
    width: 220px;
    text-align: right;
  }
  .person-name {
    font-family: "Poppins", Arial, sans-serif;
    font-weight: 700;
    font-size: 18px;
    color: var(--navy);
  }
  .person-title {
    font-size: 12.5px;
    color: var(--ink);
    margin-top: 1px;
  }
  .address {
    font-size: 13.5px;
    color: var(--ink);
    margin-top: 22px;
    line-height: 1.4;
  }
  .divider {
    position: absolute;
    left: 282px;
    top: 140px;
    width: 1px;
    height: 120px;
    background: var(--rule);
  }
  .contacts {
    position: absolute;
    left: 302px;
    top: 148px;
    list-style: none;
  }
  .contacts li {
    display: flex;
    align-items: center;
    gap: 10px;
    font-size: 13px;
    color: var(--ink);
    line-height: 23px;
  }
  .contacts svg { width: 14px; height: 14px; fill: var(--green-text); flex: none; }
  .contacts .accent { color: var(--lime-deep); }
  .base-bands {
    position: absolute;
    left: 0; bottom: 0;
    width: 560px; height: 60px;
  }
  .band-blue { fill: var(--navy); }
  .band-green { fill: var(--lime); }
</style>
</head>
<body>

<section class="card card-front" aria-label="Card front">
  <div class="wordmark">
    <span class="wordmark-dot"></span>
    <span class="wordmark-name">Delia K. Fenwick, MS, LPC</span>
  </div>
  <p class="tagline">Therapy for Individuals, Couples &amp; Families</p>
</section>

<section class="card card-back" aria-label="Card back">
  <div class="lockup">
    <div class="wordmark">
      <span class="wordmark-dot"></span>
      <span class="wordmark-name">Delia K. Fenwick, MS, LPC</span>
    </div>
    <p class="tagline">Therapy for Individuals, Couples &amp; Families</p>
  </div>

  <div class="person">
    <p class="person-name">Delia K. Fenwick, MS</p>
    <p class="person-title">Licensed Professional Counselor</p>
    <p class="address">415 Harrowgate Lane Suite<br>231 Jacksonville, NC 28593</p>
  </div>

  <div class="divider"></div>

  <ul class="contacts">
    <li>
      <svg viewBox="0 0 16 16" aria-hidden="true"><path d="M3 1h3l1.5 4-2 1.3a9 9 0 0 0 4.2 4.2L11 8.5l4 1.5v3a2 2 0 0 1-2 2A12 12 0 0 1 1 3a2 2 0 0 1 2-2z"/></svg>
      (910) 487-6124
    </li>
    <li>
      <svg viewBox="0 0 16 16" aria-hidden="true"><path d="M4 1h8v4H4z M1 6h14v7h-3v2H4v-2H1z M5 10v4h6v-4z"/></svg>
      (910) 487-6125
    </li>
    <li>
      <svg viewBox="0 0 16 16" aria-hidden="true"><path d="M8 1a7 7 0 1 0 0 14A7 7 0 0 0 8 1zm0 1.5c.8 0 1.8 1.6 2.1 4.5H5.9C6.2 4.1 7.2 2.5 8 2.5zM2.6 7h2.2c0-1.6.3-3 .8-4A5.5 5.5 0 0 0 2.6 7zm8.6 0h2.2a5.5 5.5 0 0 0-3-4c.5 1 .8 2.4.8 4zM2.6 9a5.5 5.5 0 0 0 3 4c-.5-1-.8-2.4-.8-4zm3.3 0c.3 2.9 1.3 4.5 2.1 4.5s1.8-1.6 2.1-4.5zm5.3 0c0 1.6-.3 3-.8 4a5.5 5.5 0 0 0 3-4z"/></svg>
      www.<span class="accent">deliafenwicklpc</span>.example
    </li>
    <li>
      <svg viewBox="0 0 16 16" aria-hidden="true"><path d="M1 3h14v10H1z M2 4.2v.6l6 4 6-4v-.6z" fill-rule="evenodd"/></svg>
      delia@deliafenwicklpc.example
    </li>
  </ul>

  <svg class="base-bands" viewBox="0 0 560 60" preserveAspectRatio="none" aria-hidden="true">
    <polygon class="band-green" points="330,16 560,2 560,16"/>
    <polygon class="band-blue" points="0,48 300,48 330,16 560,16 560,60 0,60"/>
  </svg>
</section>

</body>
</html>
```